letterhead design

can you create a letterhead using the logo you created and the following:

318 W Dunhaven Elgin IL 60123
(p) 847-555-0143
(f) 847-555-0178
www.thebrantleylawgroup.com

Industry/Entity Type

Law

Requirements
Must have
• Use logo attached: must have address 318 W Dunhaven Elgin IL 60123 phone 847-555-0143 fax 847-555-0178
Should not have
• Nothing other thank logo and address/phone/website

```html
<!DOCTYPE html>
<html lang="en">
<head>
<meta charset="utf-8">
<title>Brantley Law Group – Letterhead</title>
<link rel="stylesheet" href="https://fonts.googleapis.com/css2?family=Marcellus&display=swap">
<style>
  :root {
    --backdrop: #cdd3d3;
    --paper: #ffffff;
    --gold: #e1ad4c;
    --ink: #1c1c1c;
  }
  * { margin: 0; padding: 0; box-sizing: border-box; }
  html, body {
    width: 1200px;
    height: 1028px;
    overflow: hidden;
    background: var(--backdrop);
  }
  .letterhead {
    position: absolute;
    left: 260px;
    top: 34px;
    width: 680px;
    height: 960px;
    background: var(--paper);
    font-family: "Marcellus", serif;
  }
  .brand {
    position: absolute;
    top: 36px;
    left: 0;
    right: 0;
    display: flex;
    flex-direction: column;
    align-items: center;
  }
  .brand-circle {
    width: 68px;
    height: 68px;
    border: 1.5px solid var(--gold);
    border-radius: 50%;
  }
  .brand-name {
    margin-top: 10px;
    color: var(--gold);
    font-size: 24px;
    letter-spacing: 0.5px;
    line-height: 1;
  }
  .brand-sub {
    margin-top: 4px;
    display: flex;
    align-items: center;
    gap: 8px;
    color: var(--gold);
    font-size: 13px;
    letter-spacing: 1.5px;
  }
  .brand-sub::before,
  .brand-sub::after {
    content: "";
    width: 54px;
    height: 1px;
    background: var(--gold);
  }
  .footer-rule {
    position: absolute;
    left: 36px;
    right: 36px;
    top: 853px;
    height: 1.5px;
    background: var(--gold);
  }
  .contact {
    position: absolute;
    display: flex;
    align-items: center;
    gap: 8px;
    color: var(--ink);
    font-size: 15px;
    line-height: 1;
    white-space: nowrap;
  }
  .contact svg { width: 13px; height: 14px; flex: none; }
  .contact-address { top: 882px; left: 0; right: 0; justify-content: center; }
  .contact-phone   { top: 916px; left: 36px; }
  .contact-web     { top: 916px; left: 0; right: 0; justify-content: center; }
  .contact-fax     { top: 916px; right: 33px; }
</style>
</head>
<body>
  <main class="letterhead">
    <header class="brand">
      <div class="brand-circle"></div>
      <div class="brand-name">BRANTLEY LAW</div>
      <div class="brand-sub">GROUP</div>
    </header>

    <div class="footer-rule"></div>

    <p class="contact contact-address">
      <svg viewBox="0 0 14 16" aria-hidden="true"><path d="M7 1a4.5 4.5 0 0 0-4.5 4.5C2.5 9 7 13 7 13s4.5-4 4.5-7.5A4.5 4.5 0 0 0 7 1zm0 6.3A1.8 1.8 0 1 1 7 3.7a1.8 1.8 0 0 1 0 3.6z" fill="var(--gold)"/><ellipse cx="7" cy="14.3" rx="4.5" ry="1.2" fill="none" stroke="var(--gold)" stroke-width="0.9"/></svg>
      318 W Dunhaven Elgin IL 60123
    </p>
    <p class="contact contact-phone">
      <svg viewBox="0 0 14 14" aria-hidden="true"><path d="M3.2 1.2l2 2.4-1.1 1.4a7.5 7.5 0 0 0 4.9 4.9l1.4-1.1 2.4 2-1.2 1.8C7 12.5 1.5 7 1.4 2.4z" fill="var(--gold)"/><path d="M8.2 1.5a4.4 4.4 0 0 1 4.3 4.3M8.2 3.5a2.4 2.4 0 0 1 2.3 2.3" fill="none" stroke="var(--gold)" stroke-width="1"/></svg>
      847-555-0143
    </p>
    <p class="contact contact-web">
      <svg viewBox="0 0 14 14" aria-hidden="true"><circle cx="7" cy="7" r="6" fill="var(--gold)"/><path d="M4 3.5c1.5.5 1.2 2 2.4 2.4.9.3.4 1.6-.4 2-.9.4-.4 2-1.4 2.7M9 2.5c-.5 1 .6 1.5 1.5 1.4M9.5 8c.8.2 1.4 1 1.2 2" fill="none" stroke="#fff" stroke-width="0.9"/></svg>
      www.thebrantleylawgroup.com
    </p>
    <p class="contact contact-fax">
      <svg viewBox="0 0 14 14" aria-hidden="true"><rect x="1" y="5" width="3" height="8" rx="0.6" fill="var(--gold)"/><rect x="4.6" y="5" width="8.4" height="8" rx="0.6" fill="var(--gold)"/><rect x="6" y="1" width="5.6" height="3.5" fill="none" stroke="var(--gold)" stroke-width="0.9"/><path d="M6.2 7.5h1.2M8.4 7.5h1.2M10.6 7.5h1.2M6.2 9.5h1.2M8.4 9.5h1.2M10.6 9.5h1.2" stroke="#fff" stroke-width="0.9"/></svg>
      847-555-0178
    </p>
  </main>
</body>
</html>
```